Etiketten für Gin
Zielgruppe
Wir vertreiben einen regionalen Gin mit Fichtennadeln.
Zielgruppe sind Gin-Trinker, Wanderer, Besucher und Bewohner der Bergischen Landes.
Aufgabenstellung
Benötigt wird ein zweiteiliges Etikett für eine 500 ml Flasche (Höhe 320 mm, Durchmesser ca. 75 mm). Datenblatt in der Anlage. Die Flasche wird einen schwarzen Stopfen bekommen,
Das vordere Etikett soll eine Größe von 80 mm (Breite) x 160 mm (Höhe) haben. Das Etikett für die Rückseite soll eine Größe von 60 mm (Breite) x 100 mm (Höhe) haben.
Aufgrund des schwarzen Stopfens wird ein Etikett mit/in schwarz favorisiert. Auf der Vorderseite soll unser Logo (bei den Dateien) abgebildet sein.
Pflichtangaben Vorderseite: auf dem vorderen Etikett müssen die Pflichtangaben zur Nettofüllmenge und zum Alkoholgehalt angegeben sein. Sprich, auf der Vorderseite muss 500 ml und 43 % untergebracht sein. Diese Pflichtangaben müssen zwingend eine Höhe von 4 mm haben (gesetzlich vorgeschrieben). Gleiches gilt für die Verkehrsbezeichnung Gin, die im Logo enthalten ist. Das Wort Gin muss ebenfalls eine Größe von mindestens 4 mm haben.
Auf dem rückwärtigen Etikett müssen folgende Pflichtangaben vorhanden sein:
Talwerk Brand
Lukas Dornfeld
Anton-Weller-Straße 27
51467 Bergisch Gladbach
Des Weiteren wären auf der Rückseite zwei Felder wünschenswert, in die man zum einen die Batch No. und zum anderen die Flaschennummer eintragen kann (Beispiel Bild 'Batch_Flasche'). Zudem ein weißes Feld, in dem später der EAN Code Ei gepflegt werden kann.
Als Text für die Rückseite:
Wo Natur auf Geschmack trifft
Das 'Bergische Gefühl' erleben Sie mit dem Talwerk Brand Gin. Lassen Sie einen naturverbundenen Tag zum Ausklang, beispielsweise nach einer Wanderung, noch einmal an Ihnen vorbeiziehen.
Erinnern Sie sich durch die bei der Herstellung geschmacksgebenden Botanicals von der Fichte an einen erholsamen Spaziergang durch die Wälder des Bergischen Landes.
Mehr Informationen unter
www.talwerk-brand.de
Druckdatenanlieferung laut Druckerei:
Dateiform..

```html
<!DOCTYPE html>
<html lang="de">
<head>
<meta charset="utf-8">
<title>Talwerk Brand Gin – Frontetikett</title>
<link rel="stylesheet" href="https://fonts.googleapis.com/css2?family=Poiret+One&family=Oswald:wght@500&display=swap">
<style>
  :root {
    --paper: #fafaf7;
    --ink: #1b1b1b;
    --pine: #6a9a2a;
    --pine-pale: #dde4cc;
    --cutline: #e8197d;
  }
  * { margin: 0; padding: 0; box-sizing: border-box; }
  html, body { width: 1067px; height: 1200px; overflow: hidden; background: var(--paper); }
  .label {
    position: relative;
    width: 1067px;
    height: 1200px;
    background: var(--paper);
    border: 2px solid var(--cutline);
    border-radius: 4px;
    overflow: hidden;
  }
  .forest-band {
    position: absolute;
    left: 0; right: 0; bottom: 0;
    height: 410px;
    background: linear-gradient(to bottom, rgba(221,228,204,0) 0%, var(--pine-pale) 45%, var(--pine-pale) 100%);
  }
  .brand-mark {
    position: absolute;
    left: 363px; top: 163px;
    width: 340px; height: 340px;
  }
  .brand-name {
    position: absolute;
    left: 0; right: 0; top: 585px;
    text-align: center;
    font-family: "Poiret One", sans-serif;
    font-size: 132px;
    line-height: 1;
    letter-spacing: 4px;
    color: var(--ink);
    font-weight: 400;
  }
  .product-type {
    position: absolute;
    left: 0; right: 0; top: 722px;
    display: flex;
    justify-content: center;
    align-items: center;
    gap: 30px;
    font-family: "Oswald", sans-serif;
    font-weight: 500;
    font-size: 66px;
    line-height: 1;
    letter-spacing: 22px;
    color: var(--pine);
  }
  .product-type .dot {
    width: 12px; height: 12px;
    border-radius: 50%;
    background: var(--ink);
  }
  .product-type .word { margin-right: -22px; }
  .legal {
    position: absolute;
    top: 1008px;
    font-family: "Oswald", sans-serif;
    font-weight: 500;
    font-size: 60px;
    line-height: 1;
    color: var(--pine);
  }
  .legal-abv { left: 133px; }
  .legal-volume { right: 132px; }
</style>
</head>
<body>
  <main class="label">
    <div class="forest-band" role="img" aria-label="Zarte Silhouetten eines Fichtenwaldes in hellem Grün"></div>

    <svg class="brand-mark" viewBox="0 0 340 340" aria-hidden="true">
      <circle cx="170" cy="170" r="160" fill="none" stroke="var(--pine)" stroke-width="14"/>
    </svg>

    <h1 class="brand-name">TALWERK BRAND</h1>

    <p class="product-type">
      <span class="dot"></span>
      <span class="word">GIN</span>
      <span class="dot"></span>
    </p>

    <p class="legal legal-abv">43 % VOL</p>
    <p class="legal legal-volume">500 ML</p>
  </main>
</body>
</html>
```